Summer Sunglass offer

Need a poster design for a spring / summer campaign. We are an opticians with good footfall. The design needs to be eye catching and aimed at 40 year old plus. The offer is Up to 50% off sunglass offer, t&c apply. (I have attached our last year campaign)
Also need a 2 sided A5 leaflet design (see attached)
I've uploaded a copy of our logo

A5 leaflet should read:

Grab a bargain on two great looks this summer Upto 50% off sunglasses
Look great and stay safe in the sun this summer

We want you to look great, feel fantastic and most of all stay safe in the sun this summer. That’s why we’re offering you 50% off prescription sunglasses with every complete pair of glasses you buy this summer or 25% off for prescription sunglasses with no other purchase.
Find you new summer looks from our gorgeous collection of frames in store. It matters to us that you look great in your new glasses as much as how well you see through them, so we’ll be on hand to help you find frames that suit you best.
What new looks will you go for? Smart or sassy? Formal or Fun? Whatever you’re in the mood for, you’ll find it in our collections this summer.
Call in today to find your new looks, and remember to bring your prescription if you don’t need an eye test.

Target Market(s)

40 + year old

Industry/Entity Type

Optician

Colors

Designer to choose colors to be used in the design.

Requirements
Must have
• Images, preferably a male and Female image

```html
<!DOCTYPE html>
<html lang="en">
<head>
<meta charset="utf-8">
<title>Summer Sunglasses Offer Poster</title>
<link href="https://fonts.googleapis.com/css2?family=Montserrat:wght@400;500;800&display=swap" rel="stylesheet">
<style>
  :root {
    --navy: #0e1a52;
    --yellow: #ffe600;
    --teal: #2e8b92;
    --paper: #ffffff;
    --backdrop: #e9e9e7;
    --skin-light: #f1d9c8;
    --skin-mid: #d9ad92;
    --hair: #6b5545;
  }
  * { margin: 0; padding: 0; box-sizing: border-box; }
  html, body {
    width: 1200px;
    height: 1148px;
    overflow: hidden;
    background: var(--backdrop);
    font-family: "Montserrat", Arial, sans-serif;
  }
  .poster {
    position: absolute;
    left: 205px;
    top: 19px;
    width: 790px;
    height: 1110px;
    background: var(--paper);
    overflow: hidden;
  }
  .poster__shapes {
    position: absolute;
    inset: 0;
  }
  .headline {
    position: absolute;
    top: 44px;
    left: 0;
    width: 100%;
    text-align: center;
    color: var(--navy);
    font-weight: 400;
    font-size: 40px;
    line-height: 1.25;
    letter-spacing: 0.5px;
  }
  .offer-badge__text {
    position: absolute;
    left: 278px;
    top: 180px;
    width: 260px;
    color: var(--yellow);
    font-weight: 800;
    text-align: center;
    line-height: 1;
  }
  .offer-badge__upto { display: block; font-size: 38px; margin-left: 24px; }
  .offer-badge__value { display: block; font-size: 98px; letter-spacing: -2px; margin-top: 2px; }
  .offer-badge__off { display: block; font-size: 48px; text-align: right; padding-right: 18px; margin-top: -4px; }
  .tagline {
    position: absolute;
    left: 536px;
    top: 466px;
    color: var(--navy);
    font-weight: 400;
    font-size: 30px;
    line-height: 1.38;
  }
  .tagline__line:nth-child(2) { margin-left: 3px; }
  .tagline__line:nth-child(3) { margin-left: 7px; }
  .tagline__line:nth-child(4) { margin-left: 10px; }
  .tagline__line:nth-child(5) { margin-left: 13px; }
  .tagline__line--large {
    display: block;
    font-size: 50px;
    margin-left: 16px;
    line-height: 1.05;
  }
  .tagline__line { display: block; }
  .brand {
    position: absolute;
    left: 48px;
    top: 1012px;
    display: flex;
    align-items: center;
    gap: 14px;
    color: var(--teal);
    font-weight: 500;
  }
  .brand__dot {
    width: 46px;
    height: 46px;
    border-radius: 50%;
    background: var(--teal);
  }
  .brand__name { font-size: 30px; line-height: 1; letter-spacing: 0.5px; }
  .brand__sub { display: block; font-size: 16px; letter-spacing: 3px; margin-top: 4px; }
</style>
</head>
<body>
  <main class="poster">
    <svg class="poster__shapes" width="790" height="1110" viewBox="0 0 790 1110" aria-hidden="false">
      <defs>
        <linearGradient id="portrait-tone" x1="0" y1="0" x2="0" y2="1">
          <stop offset="0" stop-color="var(--hair)"/>
          <stop offset="0.15" stop-color="var(--skin-mid)"/>
          <stop offset="0.55" stop-color="var(--skin-light)"/>
          <stop offset="1" stop-color="#f4f2ef"/>
        </linearGradient>
      </defs>
      <polygon class="offer-badge" fill="var(--navy)" transform="translate(408 300) rotate(4)"
        points="150,0 126.9,16.7 144.9,38.8 118.3,49 129.9,75 101.6,77.9 106.1,106.1 77.9,101.6 75,129.9 49,118.3 38.8,144.9 16.7,126.9 0,150 -16.7,126.9 -38.8,144.9 -49,118.3 -75,129.9 -77.9,101.6 -106.1,106.1 -101.6,77.9 -129.9,75 -118.3,49 -144.9,38.8 -126.9,16.7 -150,0 -126.9,-16.7 -144.9,-38.8 -118.3,-49 -129.9,-75 -101.6,-77.9 -106.1,-106.1 -77.9,-101.6 -75,-129.9 -49,-118.3 -38.8,-144.9 -16.7,-126.9 0,-150 16.7,-126.9 38.8,-144.9 49,-118.3 75,-129.9 77.9,-101.6 106.1,-106.1 101.6,-77.9 129.9,-75 118.3,-49 144.9,-38.8 126.9,-16.7"/>
      <path class="portrait" role="img" aria-label="Photo of a woman wearing dark round glasses and a white top, hand resting at her chin"
        fill="url(#portrait-tone)"
        d="M128 960 L146 820 Q166 735 232 712 L236 560 Q252 440 340 432 Q452 426 474 530 L482 712 Q604 730 636 820 L656 955 Q400 1010 128 960 Z"/>
      <path class="swoosh" fill="var(--teal)"
        d="M432 1012 Q600 940 772 952 Q790 960 790 975 L790 1045 Q660 966 432 1012 Z"/>
    </svg>

    <h1 class="headline">GRAB A BARGAIN ON TWO<br>GREAT LOOKS THIS SUMMER</h1>

    <div class="offer-badge__text">
      <span class="offer-badge__upto">UP TO</span>
      <span class="offer-badge__value">50%</span>
      <span class="offer-badge__off">OFF</span>
    </div>

    <p class="tagline">
      <span class="tagline__line">SUNGLASSES</span>
      <span class="tagline__line">LOOK GREAT</span>
      <span class="tagline__line">AND STAY</span>
      <span class="tagline__line">SAFE IN THE</span>
      <span class="tagline__line">SUN THIS</span>
      <span class="tagline__line--large">SUMMER</span>
    </p>

    <div class="brand">
      <span class="brand__dot"></span>
      <span class="brand__name">BROOKFIELD<span class="brand__sub">EYECARE CENTRE</span></span>
    </div>
  </main>
</body>
</html>
```